Wordpress Design Project - MarbleQuay

I would like our existing old website at www.marblequay.example to be redesigned to a more modern attractive site using Wordpress, a total of 5 web pages. And also installed onto our new web hosting site. Please visit the existing website using Microsoft Internet explorer to see the content.
The new site must be compatible with all popular web browsers and mobile devices (if possible).
There should be a contact button available on each page with an associated form in case an interested person wants to contact us. This form must be spam proof not allowing automated crawlers from activating it.

There are only 5 pages web pages to this MarbleQuay project.

```html
<!DOCTYPE html>
<html lang="en">
<head>
<meta charset="utf-8">
<title>MarbleQuay — Telephonic Solutions</title>
<link rel="stylesheet" href="https://fonts.googleapis.com/css2?family=Arimo:wght@400;700&family=Cabin:wght@500;600&family=Gelasio:ital,wght@0,400;1,400&display=swap">
<style>
  :root {
    --nav-blue: #0b5aa9;
    --nav-blue-dark: #08488c;
    --ink: #1a1a1a;
    --body-text: #2b2b2b;
    --muted: #8a8a8a;
    --link: #1a3a8a;
    --rule: #cfcfcf;
    --panel: #ffffff;
    --band-gray: #e6e6e6;
    --hero-violet: #6a3fd8;
    --hero-pink: #d86ad8;
    --btn-border: #c9c9c9;
    --arrow: #2b4c9a;
  }
  * { margin: 0; padding: 0; box-sizing: border-box; }
  html, body { width: 1200px; height: 832px; overflow: hidden; background: #fff; }
  body { position: relative; font-family: "Arimo", Arial, sans-serif; color: var(--body-text); }
  .abs { position: absolute; }

  .hero-band {
    left: 0; top: 33px; width: 1200px; height: 200px;
    background:
      radial-gradient(ellipse 240px 80px at 860px 40px, rgba(216,106,216,.55), transparent 70%),
      linear-gradient(180deg, var(--hero-violet) 0%, #9c86e6 35%, #d8d2f4 70%, #f6f5fb 100%);
  }
  .gray-band {
    left: 0; top: 232px; width: 1200px; height: 80px;
    background: linear-gradient(180deg, var(--band-gray), #fff);
  }
  .top-bar {
    left: 0; top: 0; width: 1200px; height: 33px;
    background: linear-gradient(180deg, var(--nav-blue), var(--nav-blue-dark));
  }
  .brand-box {
    left: 279px; top: 0; width: 130px; height: 45px;
    background: linear-gradient(180deg, #fff, #e4e4e4);
    border: 1px solid #9aa6b8; box-shadow: 1px 2px 3px rgba(0,0,0,.35);
    display: flex; align-items: center; gap: 8px; padding-left: 8px;
  }
  .brand-mark { width: 14px; height: 14px; border-radius: 50%; background: var(--nav-blue); }
  .brand-name { font-family: "Arimo", Arial, sans-serif; font-weight: 700; font-size: 15px; color: var(--nav-blue); }
  .main-nav a {
    position: absolute; top: 12px; color: #fff; text-decoration: none;
    font-family: "Cabin", sans-serif; font-weight: 600; font-size: 10px; letter-spacing: .6px;
  }

  .hero-title {
    left: 279px; top: 93px; width: 260px;
    font-family: "Gelasio", Georgia, serif; font-size: 21px; line-height: 26px; color: var(--ink);
  }
  .hero-copy { left: 279px; top: 152px; width: 250px; font-size: 11px; line-height: 18.5px; color: #222; }

  .pill {
    height: 23px; border-radius: 12px; border: 1px solid var(--btn-border);
    background: linear-gradient(180deg, #fff, #e2e2e2);
    font-family: "Cabin", sans-serif; font-weight: 500; font-size: 10px; color: #222;
    display: flex; align-items: center; gap: 7px; padding-left: 12px;
  }
  .tri { width: 0; height: 0; border-left: 5px solid var(--arrow); border-top: 4px solid transparent; border-bottom: 4px solid transparent; }

  .slider-panel {
    left: 547px; top: 56px; width: 353px; height: 236px; background: var(--panel);
    box-shadow: 0 1px 5px rgba(0,0,0,.25);
  }
  .slide-frame {
    position: absolute; left: 9px; top: 8px; width: 336px; height: 183px;
    border: 2px solid #d6d6d6;
    background: radial-gradient(ellipse 110px 80px at 50% 50%, #3d3f44, #8b8c90 55%, #fff 100%);
  }
  .round-btn {
    width: 20px; height: 20px; border-radius: 50%; border: 1px solid var(--btn-border);
    background: linear-gradient(180deg, #fff, #dedede);
    display: flex; align-items: center; justify-content: center;
  }
  .tri-left { width: 0; height: 0; border-right: 5px solid var(--arrow); border-top: 4px solid transparent; border-bottom: 4px solid transparent; }

  .block-icon { width: 26px; height: 26px; border-radius: 4px; }
  .block-title { font-family: "Gelasio", Georgia, serif; font-size: 13px; color: #222; }
  .small-copy { font-size: 8.5px; line-height: 15.5px; color: #222; width: 236px; }
  .date { font-size: 8.5px; font-weight: 700; color: var(--muted); }
  .more-link {
    display: flex; align-items: center; gap: 7px;
    font-family: "Gelasio", Georgia, serif; font-size: 10px; color: var(--link);
  }
  .more-link .round-btn { width: 15px; height: 15px; }
  .more-link .tri { border-left-width: 4px; border-top-width: 3px; border-bottom-width: 3px; }
  .rule { height: 1px; background: var(--rule); }

  .why-title { left: 547px; top: 323px; font-family: "Gelasio", Georgia, serif; font-size: 19px; color: #111; }
  .why-copy { left: 547px; top: 353px; width: 360px; font-size: 10px; line-height: 16.4px; color: #222; }
  .section-title { font-family: "Gelasio", Georgia, serif; font-size: 15px; color: #222; }
  .service-list { list-style: none; left: 555px; top: 532px; }
  .service-list li { display: flex; align-items: center; gap: 11px; height: 21.5px; font-size: 9.5px; letter-spacing: .3px; color: #222; }
  .service-list .round-btn { width: 12px; height: 12px; }
  .service-list .tri { border-left-width: 3px; border-top-width: 3px; border-bottom-width: 3px; }
  .quote {
    left: 724px; top: 532px; width: 170px;
    font-family: "Gelasio", Georgia, serif; font-style: italic; font-size: 12px; line-height: 16.3px; color: #333;
  }
  .quote-author { left: 760px; top: 626px; width: 130px; text-align: right; font-size: 9px; font-weight: 700; color: #222; }
  .quote-company { left: 760px; top: 639px; width: 130px; text-align: right; font-size: 8px; color: #444; }

  .footer-rule { left: 0; top: 757px; width: 1200px; height: 1px; background: #d4d4d4; box-shadow: 0 1px 3px rgba(0,0,0,.08); }
  .footer-nav a { position: absolute; top: 794px; font-size: 8.5px; color: #333; text-decoration: none; letter-spacing: .2px; }
  .copyright { left: 734px; top: 794px; font-size: 8.5px; color: #333; }
</style>
</head>
<body>
  <div class="abs hero-band"></div>
  <div class="abs gray-band"></div>
  <div class="abs top-bar"></div>

  <div class="abs brand-box"><span class="brand-mark"></span><span class="brand-name">MarbleQuay</span></div>

  <nav class="main-nav">
    <a style="left:468px">HOME ▾</a>
    <a style="left:548px">SOLUTIONS</a>
    <a style="left:652px">IP, LAN AND INTERNET</a>
    <a style="left:796px">SERVICES</a>
    <a style="left:881px">CONTACT</a>
  </nav>

  <h1 class="abs hero-title">Telephonic Solutions to improve your business!</h1>
  <p class="abs hero-copy">Adipisicing elit,sed do eiusmod temporincididunt ut labore etitation ullamco laboris nisi ut aliquip ex ea commodo consequat. Duis aute irur dolor in reprehenderit in</p>

  <div class="abs pill" style="left:281px;top:257px;width:100px"><span class="tri"></span>Contact Now</div>
  <div class="abs pill" style="left:405px;top:257px;width:100px"><span class="tri"></span>Learn More</div>

  <div class="abs slider-panel">
    <div class="slide-frame" role="img" aria-label="Product photo of a black office desk phone with a display and coiled handset cord"></div>
    <div class="round-btn" style="position:absolute;left:151px;top:202px"><span class="tri-left"></span></div>
    <div class="round-btn" style="position:absolute;left:189px;top:202px"><span class="tri"></span></div>
  </div>

  <!-- Left column -->
  <div class="abs block-icon" style="left:279px;top:314px;background:#4a8ad8;border-radius:50%"></div>
  <h3 class="abs block-title" style="left:317px;top:326px">Chirper</h3>
  <p class="abs small-copy" style="left:279px;top:352px"><span style="color:var(--link)">Adipisicing</span> elit,sed do eiusmod temporincididunt ut labore etitation ullamco laboris nisi ut aliquip ex ea</p>
  <div class="abs more-link" style="left:434px;top:392px"><span class="round-btn"><span class="tri"></span></span>Follow Me</div>
  <div class="abs rule" style="left:279px;top:432px;width:236px"></div>

  <div class="abs block-icon" style="left:279px;top:451px;background:linear-gradient(135deg,#f1d7a0,#d9a65c)" role="img" aria-label="Small notepad and pencil icon"></div>
  <h3 class="abs block-title" style="left:322px;top:458px">In the Blog</h3>
  <p class="abs date" style="left:279px;top:491px">21st November 2009</p>
  <p class="abs small-copy" style="left:279px;top:503px">Adipisicing elit,sed do eiusmod temporincididunt ut labore etitation ullamco laboris nisi ut aliquip ex ea commodo consequat.</p>
  <div class="abs more-link" style="left:435px;top:551px"><span class="round-btn"><span class="tri"></span></span>Read More</div>
  <div class="abs rule" style="left:279px;top:578px;width:236px"></div>

  <div class="abs block-icon" style="left:279px;top:599px;background:linear-gradient(180deg,#f4f4f4,#bdbdbd)" role="img" aria-label="Small folded newspaper icon"></div>
  <h3 class="abs block-title" style="left:322px;top:607px">News</h3>
  <p class="abs date" style="left:279px;top:642px">21st November 2009</p>
  <p class="abs small-copy" style="left:279px;top:655px">Adipisicing elit,sed do eiusmod temporincididunt ut labore etitation ullamco laboris nisi ut aliquip ex ea commodo consequat.</p>
  <div class="abs more-link" style="left:447px;top:715px"><span class="round-btn"><span class="tri"></span></span>Read All</div>

  <!-- Right column -->
  <h2 class="abs why-title">Why MarbleQuay?</h2>
  <p class="abs why-copy">MarbleQuay provides state of the art VoIP PBX phone solutions with products tailored to small, medium, and large businesses. Our engineering team will asses your communication requirements and provide you with the best designed solution for your business needs.</p>
  <div class="abs more-link" style="left:821px;top:442px"><span class="round-btn"><span class="tri"></span></span>Learn More</div>
  <div class="abs rule" style="left:547px;top:474px;width:349px"></div>

  <h3 class="abs section-title" style="left:553px;top:504px">Services</h3>
  <ul class="abs service-list">
    <li><span class="round-btn"><span class="tri"></span></span>ABCDEFGHIJKL</li>
    <li><span class="round-btn"><span class="tri"></span></span>ABCDEFGHIJKL</li>
    <li><span class="round-btn"><span class="tri"></span></span>ABCDEFGHIJKL</li>
    <li><span class="round-btn"><span class="tri"></span></span>ABCDEFGHIJKL</li>
    <li><span class="round-btn"><span class="tri"></span></span>ABCDEFGHIJKL</li>
  </ul>

  <h3 class="abs section-title" style="left:722px;top:504px">Testemonials</h3>
  <blockquote class="abs quote">Adipisicing elit,sed do eiusmod temporincididunt ut labore etitation ullamco laboris nisi ut aliquip ex ea commodo consequat.</blockquote>
  <p class="abs quote-author">- Dr. Halvorsen</p>
  <p class="abs quote-company">Northfield Co.</p>

  <!-- Footer -->
  <div class="abs footer-rule"></div>
  <nav class="footer-nav">
    <a style="left:278px">HOME</a>
    <a style="left:348px">ABOUT</a>
    <a style="left:423px">SERVICES</a>
    <a style="left:501px">BLOG</a>
    <a style="left:561px">NEWS</a>
    <a style="left:622px">CONTACT</a>
  </nav>
  <p class="abs copyright">© 2013 marblequay.example.&nbsp; All Rights Reserved</p>
</body>
</html>
```